Performance Psychology Business Card Design + Letterhead

I require a new business card and letterhead for my consulting business. I am a psychologist working predominantly in sport psychology and organisational psychology. I consult to elite athletes and corporates.
I provide counselling services, workshops, assessments, and group sessions.
I'd like to use the colours in the logo.
My current card and letterhead is predominantly white - which I do like, but I'm up to try something different as well!
The letterhead doesn't need to have my name or title on it - but it can
The company is about success, achievement and reaching potential.
My website is at www.vexaltr.com.au
I have changed some of my contact details, so I definitely need a new card and I would like this project to go ahead.
Thank you for putting the time into my design - I'm really excited about a new card and appreciate your contribution.
*IMPORTANT: The Fax Number Should be: 07 45 18 93 06
Target Market(s)
Elite athletes and teams
Corporate clients
Industry/Entity Type
Business
Contact Information for Business Card
Dr Marika Hollbeck
Director (this is optional - I don't have to have this on there)
Level 1, 482 Wexcombe St
Townsville Qld 4810
M: 0491 263 518
F: 07 45 931 260
E: mi@vexaltr.com.au
W: www.vexaltr.com.au
Requirements
Must have
- Logo - I have one with a white background and one with blue - don't mind which one is used. Currently I have the white logo on letterhead and cards.
I would like to have the catchphrase of the company
... the best you can be
on the card somewhere.
Nice to have
- On my current card I have a few lines on the back to write appointment times for clients - however this isn't essential
I also have some of the key services provided:
- Performance Enhancement
- Assessment & Reports
- Individual & Group Counselling
- Executive coaching & Motivation
- Seminars & Workshops
I have a QR file - don't have it on my current card, but thinking it could go on the business card (probably not letterhead?). For some reason I can only load one file, so can send it through if it's needed.

```html
<!DOCTYPE html>
<html lang="en">
<head>
<meta charset="utf-8">
<title>Vexaltr Psychology – Business Card</title>
<link rel="stylesheet" href="https://fonts.googleapis.com/css2?family=Crimson+Text:wght@400;600&display=swap">
<style>
  :root {
    --paper: #ffffff;
    --wash: #edf2f9;
    --wash-deep: #e3ebf6;
    --brand-navy: #27347a;
    --brand-blue: #3499d6;
    --text-blue: #2b85c9;
    --service-blue: #1c6db3;
    --rule-light: #a9cdea;
  }
  * { margin: 0; padding: 0; box-sizing: border-box; }
  html, body {
    width: 1200px; height: 694px; overflow: hidden;
    background: var(--paper);
  }
  .card {
    position: relative; width: 1200px; height: 694px;
    background: var(--paper);
    font-family: "Crimson Text", "Palatino Linotype", serif;
    color: var(--text-blue);
  }
  .backdrop { position: absolute; inset: 0; }
  .hand-plant {
    position: absolute; left: 51px; top: 292px; width: 460px; height: 357px;
    background: linear-gradient(160deg, var(--wash-deep), var(--wash) 70%, rgba(237,242,249,0));
    border-radius: 0 60% 30% 0 / 0 45% 30% 0;
  }
  .victory-figure {
    position: absolute; left: 1069px; top: 61px; width: 72px; height: 158px;
    background: linear-gradient(180deg, var(--brand-blue), #2f8fd0);
    border-radius: 40% 40% 6px 6px / 18% 18% 6px 6px;
  }
  .brand {
    position: absolute; left: 58px; top: 120px; width: 320px;
    color: var(--brand-navy); font-weight: 400; text-align: center;
  }
  .brand-name { display: block; font-size: 84px; line-height: 84px; }
  .brand-sub { display: block; font-size: 26px; letter-spacing: 9px; line-height: 36px; margin-top: 22px; }
  .contact-rule {
    position: absolute; left: 55px; top: 218px; width: 1086px; height: 3px;
    background: var(--brand-blue);
  }
  .name, .website, .address, .fax, .mobile, .tagline { position: absolute; white-space: nowrap; }
  .name { left: 423px; top: 179px; font-size: 26px; }
  .website { right: 141px; top: 178px; font-size: 27px; }
  .address { left: 423px; top: 226px; font-size: 26px; }
  .fax { left: 423px; top: 257px; font-size: 26px; }
  .mobile { left: 679px; top: 257px; font-size: 26px; }
  .services {
    position: absolute; left: 411px; top: 350px; list-style: none;
    color: var(--service-blue); font-size: 33px;
  }
  .services li {
    line-height: 36px; margin-bottom: 9px;
    border-bottom: 1px solid var(--rule-light); width: max-content;
  }
  .tagline { right: 57px; top: 600px; font-size: 32px; letter-spacing: 0.3px; }
</style>
</head>
<body>
<main class="card">
  <svg class="backdrop" width="1200" height="694" viewBox="0 0 1200 694" aria-hidden="true">
    <path d="M51 47 H1154 V640 C1120 380 930 110 130 47 Z" fill="var(--wash)"/>
  </svg>

  <div class="hand-plant" role="img" aria-label="Faint illustration of an open hand holding a young sprouting plant"></div>
  <div class="victory-figure" role="img" aria-label="Silhouette of a person raising a fist in victory"></div>

  <div class="brand">
    <span class="brand-name">Vexaltr</span>
    <span class="brand-sub">PSYCHOLOGY</span>
  </div>

  <div class="contact-rule"></div>
  <p class="name">Dr Marika Hollbeck</p>
  <p class="website">www.vexaltr.com.au</p>
  <p class="address">Level&nbsp; 1, 482 Wexcombe St Townsville Qld 4810</p>
  <p class="fax">Fax: 07 45 931 260</p>
  <p class="mobile">Mobil: 0491 263 518</p>

  <ul class="services">
    <li>- Assessment &amp; Reports</li>
    <li>- Seminars &amp; Workshops</li>
    <li>- Performance Enhancement</li>
    <li>- Individual &amp; Group Counselling</li>
    <li>- Executive coaching &amp; Motivation</li>
  </ul>

  <p class="tagline">THE BEST YOU CAN BE</p>
</main>
</body>
</html>
```